Business Card Design

We need a basic, but modern design card. Our business is a local Queanbeyan/Canberra courier service, but can organise interstate delivery if needed. Our fleet ranges from 1 tonne vans to 8 tonne trucks.

Industry/Entity Type

Business

Contact Information for Business Card

Harbourline Freight
14 Wren Parade
Queanbeyan NSW 2620

Dean Fairley
CEO

Phone: 02 61847315
Fax: 02 61847358
email: dean@harbourlinefreight.example.au

```html
<!DOCTYPE html>
<html lang="en">
<head>
<meta charset="utf-8">
<title>Harbourline Freight – Business Card</title>
<link rel="stylesheet" href="https://fonts.googleapis.com/css2?family=Exo+2:wght@300;400;500;600&display=swap">
<style>
  :root {
    --page: #35363a;
    --card: #ffffff;
    --brand-blue: #1aa7e6;
    --band-dark: #2f3033;
    --band-dark-soft: #5a5b5e;
    --row-grey: #d3d3d3;
    --ink: #2a2a2c;
    --on-dark: #ffffff;
  }
  * { box-sizing: border-box; margin: 0; padding: 0; }
  html, body {
    width: 1200px; height: 974px; overflow: hidden;
    background: var(--page);
    font-family: "Exo 2", sans-serif;
  }
  .canvas {
    position: relative; width: 1200px; height: 974px;
    display: flex; justify-content: center; align-items: center; gap: 60px;
  }
  .card {
    position: relative; width: 420px; height: 720px;
    background: var(--card); overflow: hidden;
  }

  /* back side */
  .back .brand-name {
    position: absolute; left: 64px; top: 110px;
    font-size: 50px; font-weight: 400; line-height: 1.1;
    color: var(--brand-blue);
  }

  /* bottom tab band shared by both sides */
  .tab-band {
    position: absolute; left: 0; bottom: 0;
    width: 88%; height: 72px;
    border-top-right-radius: 30px;
    display: flex; align-items: center; padding-left: 30px;
    color: var(--on-dark); font-size: 15px; font-weight: 500; letter-spacing: .3px;
    white-space: nowrap;
  }
  .back .tab-band { background: var(--band-dark); }
  .front .tab-band { background: var(--brand-blue); height: 86px; }

  /* front side */
  .front .brand-name {
    position: absolute; right: 26px; top: 56px;
    font-size: 36px; font-weight: 400; color: var(--brand-blue);
    white-space: nowrap;
  }
  .name-band {
    position: absolute; left: 0; top: 140px; width: 100%; height: 92px;
    background: linear-gradient(90deg, var(--band-dark-soft) 0%, var(--band-dark) 45%);
    color: var(--on-dark);
    display: flex; flex-direction: column; justify-content: center;
    padding-left: 150px;
  }
  .person-name { font-size: 26px; font-weight: 500; letter-spacing: 1px; }
  .person-title { font-size: 17px; font-weight: 400; letter-spacing: 2px; margin-top: 2px; }

  .contact-row {
    position: absolute; left: 0; width: 100%;
    display: flex; align-items: center;
    color: var(--ink); font-size: 17px; font-weight: 400; line-height: 1.35;
  }
  .contact-row .icon { width: 40px; height: 40px; margin: 0 28px 0 44px; flex: none; }
  .row-phone { top: 232px; height: 112px; background: var(--card); }
  .row-email { top: 344px; height: 84px; background: var(--row-grey); font-size: 15px; }
  .row-address { top: 428px; height: 126px; background: var(--card); }
</style>
</head>
<body>
<main class="canvas">

  <section class="card back" aria-label="Card back">
    <h1 class="brand-name">Harbourline<br>Freight</h1>
    <div class="tab-band">www.harbourlinefreight.example.au</div>
  </section>

  <section class="card front" aria-label="Card front">
    <h2 class="brand-name">Harbourline Freight</h2>

    <div class="name-band">
      <p class="person-name">DEAN FAIRLEY</p>
      <p class="person-title">CEO</p>
    </div>

    <div class="contact-row row-phone">
      <svg class="icon" viewBox="0 0 40 40" aria-hidden="true">
        <path d="M4 14 Q20 4 36 14 L34 19 L27 18 L26 14 Q20 12 14 14 L13 18 L6 19 Z" fill="var(--ink)"/>
        <path d="M10 22 L15 17 L25 17 L30 22 L32 34 L8 34 Z" fill="var(--ink)"/>
        <circle cx="20" cy="26" r="4" fill="#fff"/>
      </svg>
      <p>02 61847315<br>02 61847358</p>
    </div>

    <div class="contact-row row-email">
      <svg class="icon" viewBox="0 0 40 40" aria-hidden="true">
        <rect x="4" y="10" width="32" height="22" fill="var(--ink)"/>
        <path d="M4 10 L20 23 L36 10" fill="none" stroke="var(--row-grey)" stroke-width="2"/>
      </svg>
      <p>dean@harbourlinefreight.example.au</p>
    </div>

    <div class="contact-row row-address">
      <svg class="icon" viewBox="0 0 40 40" aria-hidden="true">
        <path d="M20 4 C12 4 8 10 8 16 C8 24 20 36 20 36 C20 36 32 24 32 16 C32 10 28 4 20 4 Z" fill="var(--ink)"/>
        <circle cx="20" cy="16" r="5" fill="#fff"/>
      </svg>
      <p>14 Wren Parade<br>Queanbeyan NSW 2620</p>
    </div>

    <div class="tab-band">www.harbourlinefreight.example.au</div>
  </section>

</main>
</body>
</html>
```